Lifestyle Coaching comp needs wordpress design. We focus on strong mindsets, fitness and nutrition

BrimOak Lifestyle Coaching needs a wordpress site. Our tagline for now (may change) is Mindset Mastery.Fitness Badassery. Sustainable Nutrition
Our logo is below. Would like to see some complimentary colors to liven it up. Clients need to come to site and get immediate professional, but fun feel. They need to have the impression that we are the last destination in their journey to wellness. Blogging, workout videos, pictures

Target Market(s)

Mostly women ages 20+

Industry/Entity Type

Nutrition

Colors
33a6d7
86cae7
ceeaf6
cfdeed
5c5c5c
cbcbcb
474747

Requirements
Must have
• A strong, badass feel :) While not being intimidating
Nice to have
• Fun fonts. Love the font in my logo
Should not have
• Pics, logos of flowers, heads, fruit.

```html
<!DOCTYPE html>
<html lang="en">
<head>
<meta charset="utf-8">
<title>BrimOak Lifestyle Coaching</title>
<link rel="stylesheet" href="https://fonts.googleapis.com/css2?family=Lato:wght@400;700&family=Oswald:wght@500&display=swap">
<style>
:root{
  --brand-blue:#1f95d6;
  --brand-blue-light:#33a6d7;
  --sky:#86cae7;
  --ink:#474747;
  --ink-mid:#5c5c5c;
  --nav-active:#3b3b3b;
  --card-bg:rgba(28,30,34,.88);
  --footer-bg:#202020;
  --legal-bg:#0c0c0c;
  --white:#ffffff;
}
*{margin:0;padding:0;box-sizing:border-box}
html,body{width:1200px;height:970px;overflow:hidden;background:var(--white)}
body{position:relative;font-family:"Lato",sans-serif;color:var(--ink)}

.hero-photo{position:absolute;left:0;top:80px;width:1200px;height:720px;
  background:
    linear-gradient(180deg,rgba(140,170,195,.0) 0%,rgba(0,0,0,.05) 50%,rgba(0,0,0,.25) 100%),
    linear-gradient(180deg,#8fa7bd 0%,#c3ccd4 22%,#d9c3b7 45%,#b9a6a2 62%,#5e79b8 80%,#2e4fa8 100%);}

.site-header{position:absolute;left:0;top:0;width:1200px;height:91px}
.header-white{position:absolute;left:0;top:0;width:1200px;height:37px;background:var(--white)}
.logo-panel{position:absolute;left:0;top:0;width:400px;height:91px;background:var(--white);
  clip-path:polygon(0 0,100% 0,100% 37px,377px 91px,0 91px)}
.logo{position:absolute;left:165px;top:30px;display:flex;align-items:center;gap:10px}
.logo-dot{width:22px;height:22px;border-radius:50%;background:var(--brand-blue)}
.logo-name{font-family:"Lato",sans-serif;font-weight:700;font-size:30px;color:var(--brand-blue);letter-spacing:1px}
.contact-bar{position:absolute;right:164px;top:9px;display:flex;align-items:center;font-size:14px;color:var(--ink-mid)}
.contact-item{display:flex;align-items:center;gap:8px}
.contact-sep{width:1px;height:18px;background:#cfcfcf;margin:0 14px}
.main-nav{position:absolute;left:382px;top:37px;width:818px;height:37px;background:var(--brand-blue);
  clip-path:polygon(20px 0,100% 0,100% 100%,0 100%)}
.main-nav ul{list-style:none;display:flex;position:absolute;left:61px;top:0;height:37px}
.main-nav li{height:37px;display:flex;align-items:center;justify-content:center;color:var(--white);font-size:15.5px;border-right:1px solid rgba(255,255,255,.25)}
.main-nav li.is-active{background:var(--nav-active);font-weight:700}

.hero-tagline{position:absolute;left:0;width:1200px;top:328px;text-align:center;font-family:"Oswald",sans-serif;font-weight:500;font-size:28px;line-height:40px;color:var(--white);text-shadow:0 1px 3px rgba(0,0,0,.35)}
.play-btn{position:absolute;left:581px;top:418px}

.features{position:absolute;left:0;top:0}
.feature-card{position:absolute;top:602px;width:271px;height:163px;background:var(--card-bg);text-align:center;color:var(--white)}
.feature-icon{position:absolute;top:-59px;left:87px;width:96px;height:96px;border-radius:50%;background:var(--brand-blue);border:3px solid var(--white);display:flex;align-items:center;justify-content:center}
.feature-title{margin-top:54px;font-weight:700;font-size:16px;letter-spacing:.2px}
.feature-text{margin-top:7px;padding:0 16px;font-size:12.5px;line-height:15px;color:#e7e7e7}
.more-btn{display:inline-flex;align-items:center;gap:5px;margin-top:8px;height:22px;padding:0 11px;background:var(--brand-blue);font-weight:700;font-size:13px;color:var(--white)}
.slider-arrow{position:absolute;top:633px}

.site-footer{position:absolute;left:0;top:800px;width:1200px;height:136px;background:var(--footer-bg)}
.footer-nav{position:absolute;left:165px;top:32px;display:flex;font-size:13px;color:var(--white);letter-spacing:.3px}
.footer-nav span.sep{margin:0 12px}
.social-list{position:absolute;left:165px;top:63px;display:flex;gap:8px}
.social-list span{width:37px;height:37px;border-radius:50%;border:2px solid var(--white)}
.footer-logo{position:absolute;right:165px;top:46px;display:flex;align-items:center;gap:9px}
.footer-logo .logo-dot{background:var(--white)}
.footer-logo .logo-name{color:var(--white);font-size:28px}
.legal-bar{position:absolute;left:0;top:936px;width:1200px;height:34px;background:var(--legal-bg);color:var(--white);font-weight:700;font-size:13px;text-align:center;line-height:34px}
</style>
</head>
<body>

<div class="hero-photo" role="img" aria-label="Photo of smiling women stretching on blue mats in a bright fitness studio"></div>

<header class="site-header">
  <div class="header-white"></div>
  <div class="logo-panel">
    <div class="logo"><span class="logo-dot"></span><span class="logo-name">BrimOak</span></div>
  </div>
  <div class="contact-bar">
    <div class="contact-item">
      <svg width="15" height="15" viewBox="0 0 24 24"><path fill="#1f95d6" d="M6.6 10.8a15 15 0 0 0 6.6 6.6l2.2-2.2c.3-.3.7-.4 1-.2 1.1.4 2.3.6 3.6.6.6 0 1 .4 1 1V20c0 .6-.4 1-1 1A17 17 0 0 1 3 4c0-.6.4-1 1-1h3.5c.6 0 1 .4 1 1 0 1.3.2 2.5.6 3.6.1.3 0 .7-.2 1z"/></svg>
      <span>555-014-2288</span>
    </div>
    <span class="contact-sep"></span>
    <div class="contact-item">
      <svg width="15" height="11" viewBox="0 0 24 18"><rect width="24" height="18" rx="2" fill="#1f95d6"/><path d="M1 2l11 8 11-8" fill="none" stroke="#fff" stroke-width="2"/></svg>
      <span>hello@brimoakcoaching.com</span>
    </div>
  </div>
  <nav class="main-nav">
    <ul>
      <li class="is-active" style="width:103px">Home</li>
      <li style="width:126px">About Us</li>
      <li style="width:116px">Services</li>
      <li style="width:147px">Testimonials</li>
      <li style="width:145px;border-right:0">Contact Us</li>
    </ul>
  </nav>
</header>

<h1 class="hero-tagline">Mindset Mastery. Fitness Badassery.<br>Sustainable Nutrition</h1>
<svg class="play-btn" width="38" height="38" viewBox="0 0 38 38"><circle cx="19" cy="19" r="19" fill="#fff"/><path d="M15 11l12 8-12 8z" fill="#3b3b3b"/></svg>

<svg class="slider-arrow" style="left:111px" width="20" height="40" viewBox="0 0 20 40"><path d="M18 1L2 20l16 19" fill="none" stroke="#fff" stroke-width="1.5"/></svg>
<svg class="slider-arrow" style="left:1068px" width="20" height="40" viewBox="0 0 20 40"><path d="M2 1l16 19L2 39" fill="none" stroke="#fff" stroke-width="1.5"/></svg>

<section class="features">
  <article class="feature-card" style="left:165px">
    <div class="feature-icon">
      <svg width="50" height="30" viewBox="0 0 50 30"><rect x="4" y="6" width="6" height="18" rx="2" fill="#fff"/><rect x="40" y="6" width="6" height="18" rx="2" fill="#fff"/><rect x="10" y="10" width="4" height="10" fill="#fff"/><rect x="36" y="10" width="4" height="10" fill="#fff"/><rect x="14" y="13" width="22" height="4" fill="#fff"/></svg>
    </div>
    <h2 class="feature-title">PROPER FITNESS</h2>
    <p class="feature-text">Ut enim ad minim veniam, quis nostrud exercitation ullamco laboris nisi ut aliquip commodo consequat.</p>
    <span class="more-btn">More <svg width="14" height="14" viewBox="0 0 14 14"><circle cx="7" cy="7" r="7" fill="#fff"/><path d="M3.5 7h6M7 4l3 3-3 3" fill="none" stroke="#1f95d6" stroke-width="1.8"/></svg></span>
  </article>
  <article class="feature-card" style="left:465px">
    <div class="feature-icon">
      <svg width="44" height="36" viewBox="0 0 44 36"><path d="M4 16h36a18 18 0 0 1-36 0z" fill="none" stroke="#fff" stroke-width="3"/><path d="M12 12c0-5 4-5 4-9M22 12c0-5 4-5 4-9M32 12c0-5 4-5 4-9" fill="none" stroke="#fff" stroke-width="2.5" stroke-linecap="round"/></svg>
    </div>
    <h2 class="feature-title">RIGHT NUTRITION</h2>
    <p class="feature-text">Ut enim ad minim veniam, quis nostrud exercitation ullamco laboris nisi ut aliquip commodo consequat.</p>
    <span class="more-btn">More <svg width="14" height="14" viewBox="0 0 14 14"><circle cx="7" cy="7" r="7" fill="#fff"/><path d="M3.5 7h6M7 4l3 3-3 3" fill="none" stroke="#1f95d6" stroke-width="1.8"/></svg></span>
  </article>
  <article class="feature-card" style="left:765px">
    <div class="feature-icon">
      <svg width="40" height="40" viewBox="0 0 40 40"><g fill="#fff"><rect x="17" y="2" width="6" height="36" rx="1"/><rect x="17" y="2" width="6" height="36" rx="1" transform="rotate(45 20 20)"/><rect x="17" y="2" width="6" height="36" rx="1" transform="rotate(90 20 20)"/><rect x="17" y="2" width="6" height="36" rx="1" transform="rotate(135 20 20)"/><circle cx="20" cy="20" r="13"/></g><circle cx="20" cy="20" r="5" fill="#1f95d6"/></svg>
    </div>
    <h2 class="feature-title">STRONG MINDSETS</h2>
    <p class="feature-text">Ut enim ad minim veniam, quis nostrud exercitation ullamco laboris nisi ut aliquip commodo consequat.</p>
    <span class="more-btn">More <svg width="14" height="14" viewBox="0 0 14 14"><circle cx="7" cy="7" r="7" fill="#fff"/><path d="M3.5 7h6M7 4l3 3-3 3" fill="none" stroke="#1f95d6" stroke-width="1.8"/></svg></span>
  </article>
</section>

<footer class="site-footer">
  <nav class="footer-nav">
    <span>HOME</span><span class="sep">|</span><span>ABOUT</span><span class="sep">|</span><span>SERVICES</span><span class="sep">|</span><span>TESTIMONIALS</span><span class="sep">|</span><span>CONTACT</span>
  </nav>
  <div class="social-list"><span></span><span></span><span></span><span></span><span></span></div>
  <div class="footer-logo"><span class="logo-dot"></span><span class="logo-name">BrimOak</span></div>
</footer>
<div class="legal-bar">Copyright 2015 BrimOak Coaching. All Rights Reserved.</div>

</body>
</html>
```